Kestrel Unity Parade 2013

I am seeking to create a flyer promoting the event May Day in Sydney. The Event is a March and will be taking place on the 5th May Sunday. The Projection of the flyer should be fresh and modern but capable of encapsulating values of struggle, justice and solidarity. It is an event that started in the late 1800's in a struggle to obtain the 8 hour day.
This flyer should capture the old logo with a fresh modern interpretation.
Updates

HI All, 

Can we add the following details to design. Apologies it came late, it just got forwarded onto me. 

Twitter (logo) @KestrelUnity
Facebook (logo) Unity Kestrel 2013

Thanks

Reason: I want to allow designers the opportunity to make revisions on their existing designs.

Reason: Last minute changes are not coming through.

Target Market(s)

General Public, Union Members, Workers, advocates of social justice and democracy

Industry/Entity Type

Event

Requirements
Must have
• Event Details:
Kestrel Unity Parade
Sunday May 5th
Assembling: 11:30am
Marching: 12:00pm
Assembly Point: Brindle Street outside Tolvern Hall, Sydney
Kestrel Unity Logo (See Attachment) This logo should be manipulated to show a fresh and modern aspect to it, whilst retaing the same characteristics.

Nice to have
• Themes of the flyer should capture the following ideas:
International Workers Solidarity
Workers Rights
Fight for the 8 hour day
location being Sydney Australia
Images of
People Rallying, protesting, marching

```html
<!DOCTYPE html>
<html lang="en">
<head>
<meta charset="utf-8">
<title>Kestrel Unity Parade</title>
<link rel="stylesheet" href="https://fonts.googleapis.com/css2?family=Rubik+Dirt&family=Alegreya+Sans+SC:wght@800;900&display=swap">
<style>
  :root {
    --paper: #ece3cd;
    --paper-dark: #d6c9a9;
    --ink: #161616;
    --red: #d9141b;
    --white: #ffffff;
    --grey: #8a8a8a;
    --orange: #f39a1e;
    --orange-deep: #e96a12;
  }
  * { box-sizing: border-box; margin: 0; padding: 0; }
  html, body { width: 1086px; height: 1200px; overflow: hidden; background: var(--paper); }
  .flyer {
    position: relative; width: 1086px; height: 1200px; overflow: hidden;
    background: radial-gradient(ellipse at 50% 35%, var(--paper) 50%, var(--paper-dark) 100%);
    font-family: "Alegreya Sans SC", "Arial Black", sans-serif;
    font-weight: 900;
  }
  .backdrop-scene {
    position: absolute; left: 120px; top: 470px; width: 966px; height: 420px;
    background:
      radial-gradient(ellipse at 40% 60%, rgba(120,116,106,.35) 0%, rgba(120,116,106,0) 60%),
      linear-gradient(180deg, rgba(236,227,205,0) 0%, rgba(180,174,160,.5) 60%, rgba(150,146,136,.6) 100%);
  }
  .crowd-photo {
    position: absolute; left: 0; top: 820px; width: 1086px; height: 380px;
    background:
      radial-gradient(ellipse at 30% 45%, rgba(170,160,140,.55) 0%, rgba(170,160,140,0) 35%),
      radial-gradient(ellipse at 70% 40%, rgba(160,150,132,.5) 0%, rgba(160,150,132,0) 30%),
      radial-gradient(ellipse at 12% 70%, rgba(120,112,100,.5) 0%, rgba(120,112,100,0) 30%),
      linear-gradient(180deg, rgba(160,156,146,0) 0%, #6e6a62 22%, #3a3835 55%, #1e1d1b 100%);
  }
  .committee-badge {
    position: absolute; left: 40px; top: 70px; width: 210px; height: 210px;
    border-radius: 50%; background: radial-gradient(circle, var(--orange) 55%, var(--orange-deep) 100%);
    display: flex; align-items: center; justify-content: center; text-align: center;
    color: var(--white); font-size: 28px; line-height: 1.05; padding: 30px;
  }
  .title {
    position: absolute; left: 270px; top: 28px; width: 800px; text-align: center;
    font-family: "Rubik Dirt", "Impact", sans-serif; font-weight: 400; text-transform: uppercase;
    color: var(--ink); line-height: .92;
  }
  .title-city { display: block; font-size: 140px; }
  .title-sub { display: block; font-size: 92px; }
  .title-sub .accent { color: var(--red); }
  .date-banner {
    position: absolute; left: 370px; top: 300px; width: 760px; height: 80px;
    background: var(--red); transform: rotate(-4deg);
    box-shadow: -14px 16px 0 var(--grey);
    color: var(--white); font-size: 56px; line-height: 80px; padding-left: 40px;
  }
  .time-band {
    position: absolute; height: 86px; background: var(--ink);
    color: var(--white); font-size: 54px; line-height: 86px; white-space: nowrap;
  }
  .time-band .label { color: var(--red); }
  .time-assemble { left: -20px; top: 440px; width: 690px; padding-left: 170px; transform: rotate(-5deg); }
  .time-march { left: 420px; top: 590px; width: 700px; padding-left: 40px; transform: rotate(-2deg); }
  .fist-icon {
    position: absolute; left: 830px; top: 385px; width: 170px; height: 190px;
    background: radial-gradient(ellipse at 50% 40%, #3a3835 0%, #2a2927 60%, rgba(42,41,39,0) 72%);
  }
  .venue {
    position: absolute; left: 300px; top: 700px; width: 620px; height: 180px;
    background: var(--red); transform: rotate(-5deg); border-radius: 8px 30px 12px 26px;
    color: var(--white); font-size: 44px; line-height: 1.12; text-align: center;
    display: flex; align-items: center; justify-content: center;
  }
  .social {
    position: absolute; left: 0; bottom: 30px; width: 1086px;
    display: flex; justify-content: center; gap: 60px;
    color: var(--white); font-size: 34px;
  }
  .social-item { display: flex; align-items: center; gap: 14px; }
  .social-dot { width: 22px; height: 22px; border-radius: 50%; background: var(--red); }
</style>
</head>
<body>
<main class="flyer">
  <div class="backdrop-scene" role="img" aria-label="Faded photo of a Sydney harbour landmark behind the event details"></div>
  <div class="crowd-photo" role="img" aria-label="Black and white photo of a crowd of workers rallying with placards"></div>

  <div class="committee-badge">Kestrel Unity Committee</div>

  <h1 class="title">
    <span class="title-city">Kestrel</span>
    <span class="title-sub"><span class="accent">Unity</span> Parade</span>
  </h1>

  <div class="date-banner">Sunday, May 5th</div>

  <div class="time-band time-assemble"><span class="label">Assembling:</span> 11:30am</div>

  <div class="fist-icon" role="img" aria-label="Raised fist illustration"></div>

  <div class="time-band time-march"><span class="label">Marching:</span> 12:00pm</div>

  <div class="venue"><p>Brindle Street<br>outside Tolvern Hall,<br>Sydney</p></div>

  <footer class="social">
    <span class="social-item"><span class="social-dot"></span>@KestrelUnity</span>
    <span class="social-item"><span class="social-dot"></span>Unity Kestrel 2013</span>
  </footer>
</main>
</body>
</html>
```